New website

We ned to create a new website that reflects more who we are. We are delivering exclusive premium products to our customers and the current website does not reflect our products at all.
We believe in less is more and need a webpage that is clean yet professional and exclusive.

Target Market(s)

Dentistry

Industry/Entity Type

Dental

Number of Pages Required

5+ page

Font styles to use
Sans Serif

Colors

Designer to choose colors to be used in the design.

Requirements
Must have
• Picture gallery
• Nice structure
• Clean layout
Nice to have
• Light fonts
Should not have
• Any italic font styles

```html
<!DOCTYPE html>
<html lang="en">
<head>
<meta charset="utf-8">
<title>Lumadent – Smile Gallery</title>
<link rel="stylesheet" href="https://fonts.googleapis.com/css2?family=Inter:wght@300;400;500;600;700;800&display=swap">
<style>
  :root {
    --teal: #22d3cf;
    --teal-deep: #1fb6c4;
    --cyan-text: #2bbfcf;
    --navy: #283142;
    --navy-text: #2b3446;
    --coral: #ec5c57;
    --white: #ffffff;
    --muted: #7d8593;
    --body-text: #555b63;
  }
  * { margin: 0; padding: 0; box-sizing: border-box; }
  html, body { width: 1200px; height: 1001px; overflow: hidden; background: var(--white); }
  body { position: relative; font-family: "Inter", Helvetica, Arial, sans-serif; }

  .hero {
    position: absolute; left: 0; top: 0; width: 1200px; height: 395px;
    background: linear-gradient(100deg, #23d8d3 0%, #22d0d0 45%, #33b8c3 75%, #2ea2b4 100%);
  }
  .hero-photo {
    position: absolute; left: 640px; top: 0; width: 560px; height: 395px;
    background: radial-gradient(ellipse at 65% 45%, rgba(40,120,140,0.45) 0%, rgba(35,180,190,0.15) 55%, rgba(34,210,208,0) 80%);
  }
  .brand {
    position: absolute; left: 45px; top: 42px;
    display: flex; flex-direction: column; align-items: center; gap: 10px;
    color: var(--white);
  }
  .brand-mark { width: 26px; height: 20px; background: var(--white); }
  .brand-name { font-size: 17px; font-weight: 300; letter-spacing: 6px; }

  .main-nav {
    position: absolute; left: 288px; top: 76px;
    display: flex; gap: 26px;
    font-size: 12.5px; font-weight: 600; letter-spacing: 0.6px; color: var(--white);
  }
  .main-nav .current { color: var(--navy-text); }

  .lang-switch {
    position: absolute; left: 1104px; top: 40px;
    font-size: 9.5px; font-weight: 600; color: var(--white);
  }
  .lang-switch .active { color: var(--coral); }

  .page-title {
    position: absolute; left: 102px; top: 218px;
    font-size: 45px; font-weight: 800; letter-spacing: 2.5px; color: var(--white);
  }

  .gallery-index {
    position: absolute; left: 0; top: 395px; width: 388px; height: 516px;
    background: var(--navy);
  }
  .smile-list { list-style: none; position: absolute; left: 168px; top: 30px; }
  .smile-list li {
    height: 47.2px; font-size: 22px; font-weight: 400; color: var(--white);
    letter-spacing: 0.5px;
  }
  .smile-list li.faded { color: var(--muted); }
  .smile-list li.current { color: var(--coral); font-weight: 700; font-size: 26px; letter-spacing: 1px; }
  .pager { position: absolute; left: 104px; top: 187px; }

  .case {
    position: absolute; left: 448px; top: 463px; width: 660px;
  }
  .case-title {
    font-size: 21px; font-weight: 300; letter-spacing: 1.2px; color: var(--cyan-text);
  }
  .case-text {
    margin-top: 10px; font-size: 13.2px; line-height: 20px; font-weight: 400; color: var(--body-text);
  }
  .comparison { position: absolute; top: 592px; width: 296px; }
  .comparison.before { left: 448px; }
  .comparison.after { left: 801px; }
  .comparison-photo {
    width: 296px; height: 198px; border: 2px solid #1e1e1e;
    background: radial-gradient(ellipse at 50% 50%, #d9c7b1 0%, #9a5f4c 30%, #7e4a38 60%, #6a3c2d 100%);
  }
  .after .comparison-photo {
    background: radial-gradient(ellipse at 50% 48%, #f1efe8 0%, #b9807a 30%, #87503f 60%, #6d3e30 100%);
  }
  .comparison-label {
    margin-top: 31px; text-align: center;
    font-size: 20px; font-weight: 500; letter-spacing: 2px;
  }
  .before .comparison-label { color: var(--navy-text); }
  .after .comparison-label { color: var(--cyan-text); }

  .site-footer {
    position: absolute; left: 0; top: 911px; width: 1200px; height: 90px;
    background: var(--coral);
    display: flex; align-items: center; justify-content: center;
    font-size: 9.5px; color: var(--white);
  }
</style>
</head>
<body>
  <header class="hero">
    <div class="hero-photo" role="img" aria-label="Smiling woman with a bright natural smile, tinted teal"></div>

    <div class="brand">
      <span class="brand-mark"></span>
      <span class="brand-name">LUMADENT</span>
    </div>

    <nav class="main-nav">
      <span>WELCOME</span>
      <span>PRODUCTS</span>
      <span>SPECIAL SERVICES</span>
      <span class="current">SMILE GALLERY</span>
      <span>THE COMPANY</span>
      <span>SHADE ANALYSIS</span>
      <span>CONTACT</span>
    </nav>

    <div class="lang-switch"><span class="active">ENG</span> | SWE</div>

    <h1 class="page-title">SMILE GALLERY</h1>
  </header>

  <aside class="gallery-index">
    <ul class="smile-list">
      <li class="faded">SMILE 1</li>
      <li>SMILE 2</li>
      <li>SMILE 3</li>
      <li>SMILE 4</li>
      <li class="current">SMILE 5</li>
      <li>SMILE 6</li>
      <li>SMILE 7</li>
      <li>SMILE 8</li>
      <li class="faded">SMILE 9</li>
      <li class="faded">SMILE 10</li>
    </ul>
    <svg class="pager" width="12" height="114" viewBox="0 0 12 114" aria-hidden="true">
      <g fill="none" stroke="#ffffff" stroke-width="1">
        <circle cx="6" cy="3" r="2.2"/>
        <circle cx="6" cy="15" r="2.2"/>
        <circle cx="6" cy="27" r="2.6"/>
        <circle cx="6" cy="53" r="2.6"/>
        <circle cx="6" cy="66" r="2.6"/>
        <circle cx="6" cy="79" r="2.2"/>
        <circle cx="6" cy="90" r="2.2"/>
        <circle cx="6" cy="102" r="2.2"/>
        <circle cx="6" cy="113" r="2"/>
      </g>
      <circle cx="6" cy="40" r="5" fill="none" stroke="#ec5c57" stroke-width="1.2"/>
      <circle cx="6" cy="40" r="2.8" fill="#ec5c57"/>
    </svg>
  </aside>

  <main>
    <section class="case">
      <h2 class="case-title">CERAMIC CROWNS</h2>
      <p class="case-text">This patient had problems with seveere discoloration and with filling that where unaesthetic. Lumadent provided 6 fullceramic crowns to restore the beauty of a natural smile.</p>
    </section>

    <figure class="comparison before">
      <div class="comparison-photo" role="img" aria-label="Close-up of the patient's discoloured teeth before treatment"></div>
      <figcaption class="comparison-label">BEFORE</figcaption>
    </figure>

    <figure class="comparison after">
      <div class="comparison-photo" role="img" aria-label="Close-up of the patient's restored white teeth after ceramic crowns"></div>
      <figcaption class="comparison-label">AFTER</figcaption>
    </figure>
  </main>

  <footer class="site-footer">
    Lumadent AB &nbsp;-&nbsp; Box 51807 &nbsp;-&nbsp; 21530 Malmö, Sverige &nbsp;-&nbsp; Tel: +46-40-12 34 56
  </footer>
</body>
</html>
```